Technical Redesign of AI-Generated Method & Topic Graphics for PowerPoint

e have a set of graphics and diagrams that were initially created using AI. The content, structure, and overall layout are already defined and should remain largely unchanged.

The objective is NOT to create completely new designs. This is primarily a technical refinement and conversion project. The graphics need to be professionally redrawn, cleaned up, and rebuilt so that they:

• Look less AI-generated and more professional/corporate
• Match our existing corporate website style
• Are fully editable in Microsoft PowerPoint
• Use consistent fonts, colors, spacing, and iconography
• Maintain the original meaning and information structure

REFERENCE WEBSITE
https://moorwald-forschung. at/

Please use the website as the primary reference for:
• Color palette
• Typography
• Visual language
• General corporate look and feel
• Professional, research-oriented appearance

The style should be clean, technical, modern, and suitable for a scientific/research institution.

SCOPE OF WORK
For each supplied graphic:

1. Recreate the graphic manually
- Do not simply trace or export the AI image.
- Rebuild all elements using PowerPoint native objects where possible.

2. Improve visual quality
- Remove typical AI-generated inconsistencies.
- Correct alignment, spacing, proportions, and visual hierarchy.
- Standardize icons and graphic elements.

3. Corporate style adaptation
- Apply colors and typography consistent with our website.
- Use a professional and technically oriented visual style.
- Avoid decorative or overly creative design elements.

4. Ensure full editability
- All text must remain editable.
- Shapes should be editable PowerPoint objects.
- Icons should preferably be vector-based.
- Elements should not be flattened into images unless absolutely necessary.

DELIVERABLES
Required output:

• Microsoft PowerPoint (.pptx)
• All graphics fully editable
• Layered and logically grouped objects
• Consistent formatting across all graphics
• Optional source files (.svg, .ai, or . eps) if available

DESIGN DIRECTION
Please focus on:

• Technical accuracy
• Professional presentation quality
• Corporate consistency
• PowerPoint usability

Please do NOT focus on:
• Creating alternative concepts
• Artistic reinterpretations
• Major layout changes
• Creative redesigns

The goal is to transform existing AI-generated diagrams into professional, corporate-standard, PowerPoint-editable graphics that fit seamlessly with the Moorwaldinstitut Graz website and presentation materials.

```html
<!DOCTYPE html>
<html lang="en">
<head>
<meta charset="utf-8">
<title>Method Graphics – Moorwaldinstitut Graz</title>
<link rel="stylesheet" href="https://fonts.googleapis.com/css2?family=Source+Sans+3:wght@300;400;600;700&display=swap">
<style>
:root{
  --bg:#474747;
  --green:#5e7d10;
  --green-2:#7b9a2e;
  --green-3:#9bb15f;
  --green-text:#5b7a0c;
  --accent:#b8d96a;
  --teal:#0e4f44;
  --teal-soft:#c3dad3;
  --lime-soft:#eef3dd;
  --lime-icon:#e1e9c9;
  --grey-soft:#f3f3f3;
  --grey-dark:#4b4b4b;
  --grey-mid:#a0a0a0;
  --border:#98a96a;
  --border-grey:#b9b9b9;
  --ink:#3c3c3c;
  --white:#ffffff;
}
*{box-sizing:border-box;margin:0;padding:0}
html,body{width:820px;height:1200px;overflow:hidden}
body{background:var(--bg);font-family:"Source Sans 3",sans-serif;color:var(--ink);position:relative}
.slide{position:absolute;left:80px;width:1137px;height:640px;background:var(--white);transform:scale(.58);transform-origin:0 0;overflow:hidden;box-shadow:0 10px 30px rgba(0,0,0,.45)}
.slide--ipa{top:28px}.slide--mcda{top:414px}.slide--pre{top:800px}
.abs{position:absolute}
.hdr{height:91px;background:var(--green);color:var(--white);text-align:center;padding-top:22px}
.hdr h2{font-size:30px;font-weight:600;line-height:32px}
.hdr p{font-size:22px;font-weight:300;line-height:26px}
.card{position:absolute;border:1.5px solid var(--border);border-radius:4px;background:var(--white);padding:12px 20px}
.card--lime{background:var(--lime-soft)}
.card--grey{background:var(--grey-soft);border-color:var(--border-grey)}
.card--teal{background:var(--teal-soft);border-color:#7fa89c}
.card-title{display:flex;align-items:center;gap:10px;color:var(--green-text);font-weight:600;font-size:14px;line-height:15px;padding-bottom:6px;border-bottom:1px solid #c4cca8;margin-bottom:10px}
.card--grey .card-title{color:var(--ink);border-color:#c8c8c8}
.card--teal .card-title{color:var(--teal);border-color:#8fb2a8}
ul.bul{list-style:none;font-size:11px;line-height:15px}
ul.bul li{position:relative;padding-left:10px}
ul.bul li::before{content:"";position:absolute;left:0;top:6px;width:4px;height:4px;border-radius:50%;background:var(--green)}
.ico{width:34px;height:34px;flex:none;color:var(--green-text)}
.ico svg{width:100%;height:100%;fill:none;stroke:currentColor;stroke-width:1.6;stroke-linecap:round;stroke-linejoin:round}
.tri-r{width:0;height:0;border-top:10px solid transparent;border-bottom:10px solid transparent;border-left:13px solid var(--green)}
.tri-r.sm{border-top-width:5px;border-bottom-width:5px;border-left-width:7px}
.tri-d{width:0;height:0;border-left:7px solid transparent;border-right:7px solid transparent;border-top:9px solid var(--green)}
.footer{position:absolute;left:41px;top:598px;display:flex;align-items:center;gap:6px;color:var(--green-text);font-size:12px}
.footer-line{position:absolute;left:455px;top:607px;width:495px;height:1px;background:#d0d0d0}
.brand{position:absolute;right:41px;top:578px;display:flex;align-items:center;gap:6px;color:var(--green-text);font-weight:700;font-size:16px}
.brand-dot{width:14px;height:14px;border-radius:50%;border:2px solid var(--green-text)}
.pattern{position:absolute;border-radius:50%;background:radial-gradient(circle,rgba(140,150,120,.10),rgba(140,150,120,0) 70%)}
.bar{position:absolute;background:var(--teal);border-radius:3px;color:var(--white)}
.bar-title{color:var(--accent);font-weight:600}
.bar ul.bul li::before{background:var(--accent);width:6px;height:6px;top:5px}
.round-ico{border:2px solid var(--white);border-radius:50%;display:flex;align-items:center;justify-content:center;color:var(--white)}
.round-ico svg{fill:none;stroke:currentColor;stroke-width:1.8;stroke-linecap:round;stroke-linejoin:round}

/* slide 1 process */
.proc-step{position:absolute;width:52px;height:52px;border-radius:50%;background:var(--lime-icon);display:flex;align-items:center;justify-content:center;color:var(--green-text)}
.proc-step svg{width:28px;height:28px;fill:none;stroke:currentColor;stroke-width:1.8;stroke-linecap:round;stroke-linejoin:round}
.proc-label{position:absolute;width:110px;text-align:center;font-weight:600;font-size:14px;color:var(--green-text)}
.proc-dot{position:absolute;width:8px;height:8px;border-radius:50%;background:var(--green)}

/* slide 2 steps */
.step{position:absolute;top:272px;width:191px;height:175px;border:1.5px solid var(--border);border-radius:3px;padding:14px 8px 8px 8px}
.step .num{position:absolute;left:-4px;top:-10px;width:18px;height:18px;border-radius:50%;background:var(--green);color:var(--white);font-size:12px;font-weight:600;display:flex;align-items:center;justify-content:center}
.step .card-title{font-size:13px;color:var(--ink);padding:0 0 8px 8px}
.step ul.bul{font-size:10.5px;line-height:15px}
.mcda-item{display:flex;align-items:center;gap:8px;font-size:11px;line-height:14px;padding:0 10px;border-left:1px solid rgba(255,255,255,.35)}
.mcda-item svg{width:34px;height:34px;flex:none}

/* slide 3 */
.chev{position:absolute;top:98px;height:45px;color:var(--white);font-size:12px;font-weight:600;line-height:12px;display:flex;align-items:center;gap:6px;padding-left:18px;clip-path:polygon(0 0,calc(100% - 16px) 0,100% 50%,calc(100% - 16px) 100%,0 100%,16px 50%)}
.chev:first-child{clip-path:polygon(0 0,calc(100% - 16px) 0,100% 50%,calc(100% - 16px) 100%,0 100%)}
.chev .n{width:17px;height:17px;border-radius:50%;border:1.5px solid var(--white);display:flex;align-items:center;justify-content:center;font-size:11px;flex:none}
.col{position:absolute;top:150px;height:172px;padding:0 8px 0 10px}
.col + .col{border-left:1px solid #cfcfcf}
.col .ico{margin:4px auto 10px;display:block}
.col ul.bul{font-size:10.5px;line-height:15px}
.methods{position:absolute;left:41px;top:322px;width:1055px;height:50px;border:1.5px solid var(--border);border-radius:3px;display:flex;align-items:center}
.method{flex:1;display:flex;align-items:center;gap:6px;font-size:10px;line-height:11px;padding:0 8px;border-left:1px solid #d0d0d0}
.method:first-child{border-left:none}
.method .ico{width:28px;height:28px}
.kr-label{position:absolute;left:0;width:1137px;top:380px;text-align:center;font-size:12px;font-weight:700;color:var(--teal)}
.kr-line{position:absolute;top:388px;height:1px;background:#bbb}
.result{position:absolute;top:397px;height:83px;background:var(--lime-soft);border-radius:3px;display:flex;gap:6px;padding:8px}
.result .ico{width:40px;height:40px}
.result h4{font-size:13px;font-weight:600;color:var(--green-text);line-height:13px;margin-bottom:2px}
.result p{font-size:10.5px;line-height:13px}
.ben-item{display:flex;align-items:center;gap:8px;font-size:9.5px;line-height:11px;padding:0 10px;border-left:1px solid rgba(255,255,255,.35)}
.ben-item:first-child{border-left:none}
.ben-item svg{width:30px;height:30px;flex:none;fill:none;stroke:var(--white);stroke-width:1.6;stroke-linecap:round;stroke-linejoin:round}
</style>
</head>
<body>

<!-- ============ SLIDE 1 ============ -->
<section class="slide slide--ipa">
  <header class="hdr">
    <h2>Integrated Process Assessment for Technology and Product Innovation</h2>
    <p>Ecological, social and economic assessment in early development phases</p>
  </header>
  <div class="pattern" role="img" aria-label="Faint network pattern" style="left:-20px;top:400px;width:140px;height:160px"></div>
  <div class="pattern" role="img" aria-label="Faint network pattern" style="left:1000px;top:380px;width:160px;height:180px"></div>

  <div class="card" style="left:41px;top:112px;width:312px;height:141px">
    <div class="card-title"><span class="ico" style="width:30px;height:30px"><svg viewBox="0 0 32 32"><circle cx="16" cy="16" r="13"/><path d="M10 20c4-1 8-5 12-10M12 12h4v4"/></svg></span>Starting Point &amp;<br>Methodological Foundations</div>
    <ul class="bul">
      <li>Products, processes, services and systems</li>
      <li>Market, societal and sustainability requirements</li>
      <li>Goal and scope definition</li>
      <li>Reference system, data basis</li>
      <li>Scenarios and sensitivities</li>
    </ul>
  </div>
  <div class="tri-r abs" style="left:363px;top:173px"></div>

  <div class="card" style="left:386px;top:112px;width:710px;height:141px">
    <div class="abs" style="left:0;top:10px;width:100%;text-align:center;color:var(--green-text);font-weight:600;font-size:15px">Assessment Along The Innovation Process</div>
  </div>
  <div class="abs" style="left:476px;top:221px;width:530px;height:2px;background:var(--green)"></div>
  <div class="proc-step" style="left:450px;top:157px"><svg viewBox="0 0 28 28"><circle cx="12" cy="12" r="8"/><path d="M18 18l7 7"/></svg></div>
  <div class="proc-step" style="left:556px;top:157px"><svg viewBox="0 0 28 28"><path d="M10 19c0-4-4-5-4-10a8 8 0 0116 0c0 5-4 6-4 10zM11 23h6M14 1v-1M3 9H1M27 9h-2"/></svg></div>
  <div class="proc-step" style="left:662px;top:157px"><svg viewBox="0 0 28 28"><circle cx="14" cy="14" r="4"/><path d="M14 3v4M14 21v4M3 14h4M21 14h4M6 6l3 3M19 19l3 3M22 6l-3 3M9 19l-3 3"/></svg></div>
  <div class="proc-step" style="left:768px;top:157px"><svg viewBox="0 0 28 28"><path d="M14 3l10 5v12l-10 5-10-5V8zM4 8l10 5 10-5M14 13v12"/></svg></div>
  <div class="proc-step" style="left:874px;top:157px"><svg viewBox="0 0 28 28"><path d="M4 24V12l6 4v-4l6 4V6h4v18zM8 20h2M13 20h2M18 20h2"/></svg></div>
  <div class="proc-step" style="left:980px;top:157px"><svg viewBox="0 0 28 28"><path d="M5 24v-6M11 24v-9M17 24v-12M23 24v-16M4 14l7-6 5 3 8-7M20 4h4v4"/></svg></div>
  <div class="tri-r sm abs" style="left:527px;top:178px"></div>
  <div class="tri-r sm abs" style="left:633px;top:178px"></div>
  <div class="tri-r sm abs" style="left:739px;top:178px"></div>
  <div class="tri-r sm abs" style="left:845px;top:178px"></div>
  <div class="tri-r sm abs" style="left:951px;top:178px"></div>
  <div class="proc-dot" style="left:472px;top:218px"></div>
  <div class="proc-dot" style="left:578px;top:218px"></div>
  <div class="proc-dot" style="left:684px;top:218px"></div>
  <div class="proc-dot" style="left:790px;top:218px"></div>
  <div class="proc-dot" style="left:896px;top:218px"></div>
  <div class="proc-dot" style="left:1002px;top:218px"></div>
  <div class="proc-label" style="left:421px;top:228px">Research</div>
  <div class="proc-label" style="left:527px;top:228px">Concept</div>
  <div class="proc-label" style="left:633px;top:228px">Concept</div>
  <div class="proc-label" style="left:739px;top:228px">Concept</div>
  <div class="proc-label" style="left:845px;top:228px">Pilot</div>
  <div class="proc-label" style="left:951px;top:228px">Market Uptake</div>

  <div class="card card--lime" style="left:41px;top:266px;width:339px;height:137px">
    <div class="card-title">Environmental Life Cycle Assessment (eLCA)</div>
    <div style="display:flex;gap:14px;align-items:center;margin-top:14px">
      <span class="ico" style="width:48px;height:48px"><svg viewBox="0 0 32 32"><circle cx="16" cy="13" r="10"/><path d="M6 13h20M16 3c-4 4-4 16 0 20M16 3c4 4 4 16 0 20M5 22c5 0 9 3 11 7M27 22c-5 0-9 3-11 7"/></svg></span>
      <ul class="bul" style="font-size:10.5px">
        <li>Quantification of environmental impacts and benefits</li>
        <li>Comparison with a reference system</li>
        <li>Carbon footprint and broader impact categories</li>
        <li>ISO 14040/44, accredited models and databases</li>
      </ul>
    </div>
  </div>
  <div class="card card--grey" style="left:399px;top:266px;width:339px;height:137px">
    <div class="card-title">Social Life Cycle Assessment (S-LCA)</div>
    <div style="display:flex;gap:12px;align-items:center;margin-top:8px">
      <span class="ico" style="width:46px;height:46px;color:#555"><svg viewBox="0 0 32 32"><circle cx="16" cy="16" r="14"/><circle cx="11" cy="11" r="2.5"/><circle cx="21" cy="11" r="2.5"/><path d="M6 19c0-3 2-4 5-4s5 1 5 4M16 19c0-3 2-4 5-4s5 1 5 4M10 23l4 3 4-3"/></svg></span>
      <ul class="bul" style="font-size:10.5px">
        <li>Assessment of social impacts across the life cycle</li>
        <li>Working conditions, health &amp; safety, human rights</li>
        <li>Stakeholder perspective and global value chains</li>
        <li>Social hotspot identification and relevant databases</li>
      </ul>
    </div>
  </div>
  <div class="card card--teal" style="left:757px;top:266px;width:339px;height:137px">
    <div class="card-title">Life Cycle Costing (LCC)</div>
    <div style="display:flex;gap:12px;align-items:center;margin-top:8px">
      <span class="ico" style="width:46px;height:46px;color:var(--teal)"><svg viewBox="0 0 32 32"><circle cx="11" cy="9" r="7"/><path d="M14 6a4 4 0 100 6M7 8h5M7 10h5M4 30v-6M10 30v-8M16 30v-11M22 30v-14M28 30v-18M3 21l9-5 6 2 10-8"/></svg></span>
      <ul class="bul" style="font-size:10.5px">
        <li>Economic assessment across the life cycle</li>
        <li>Cost-benefit and techno-economic evaluation</li>
        <li>Infrastructure analyses and market screening</li>
        <li>Roll-out scenarios and cost drivers</li>
      </ul>
    </div>
  </div>

  <svg class="abs" style="left:0;top:0" width="1137" height="640">
    <path d="M212 403v36h218M924 403v36h-218" fill="none" stroke="#6b7f3a" stroke-width="1.5"/>
    <path d="M1123 183v339h-150" fill="none" stroke="#6b7f3a" stroke-width="1.5" stroke-dasharray="5 4"/>
    <path d="M1113 183l-8-4v8zM965 522l8-4v8z" fill="#5e7d10"/>
  </svg>

  <div class="card" style="left:430px;top:414px;width:276px;height:50px;padding:6px 14px;display:flex;align-items:center;gap:12px">
    <span class="ico" style="width:34px;height:34px;color:var(--teal)"><svg viewBox="0 0 32 32" stroke-width="3"><path d="M16 4a12 12 0 0110 5M28 16a12 12 0 01-5 10M16 28a12 12 0 01-10-5M4 16a12 12 0 015-10"/></svg></span>
    <span style="color:var(--green-text);font-weight:600;font-size:14px;line-height:15px">Balancing ecology, social aspects and economy</span>
  </div>
  <div class="tri-d abs" style="left:562px;top:464px"></div>

  <div class="bar" style="left:176px;top:473px;width:784px;height:90px;display:flex;align-items:center">
    <div style="width:112px;display:flex;justify-content:center;border-right:1px solid rgba(255,255,255,.35);height:64px;align-items:center">
      <div class="round-ico" style="width:66px;height:66px"><svg width="36" height="36" viewBox="0 0 32 32"><rect x="7" y="5" width="18" height="24" rx="2"/><path d="M12 5V3h8v2M10 12l2 2 3-3M17 12h5M10 19l2 2 3-3M17 19h5"/><circle cx="24" cy="25" r="4"/><path d="M22 25l1.5 1.5 2.5-3"/></svg></div>
    </div>
    <div style="padding-left:28px">
      <div class="bar-title" style="font-size:17px;margin-bottom:8px">Integrated Process Assessment – Concrete Benefits</div>
      <div style="display:flex;gap:40px">
        <ul class="bul"><li>Early identification of opportunities and risks</li><li>Sound decision support</li><li>Comparison of technologies and product options</li></ul>
        <ul class="bul"><li>Iterative feedback for development decisions</li><li>Holistic view of ecological, social and economic performance</li></ul>
      </div>
    </div>
  </div>

  <div class="footer"><svg width="11" height="11" viewBox="0 0 12 12" fill="none" stroke="#5b7a0c"><circle cx="6" cy="6" r="5"/><path d="M1 6h10M6 1c-2 2-2 8 0 10M6 1c2 2 2 8 0 10"/></svg>Broadly applicable to diverse technologies, processes and products</div>
  <div class="footer-line"></div>
  <div class="brand"><span class="brand-dot"></span>Moorwaldinstitut Graz</div>
</section>

<!-- ============ SLIDE 2 ============ -->
<section class="slide slide--mcda">
  <header class="hdr">
    <h2>Multi-Criteria Decision Analysis (MCDA)</h2>
    <p>From raw parameters to transparent technology ranking</p>
  </header>
  <div class="pattern" role="img" aria-label="Faint network pattern" style="left:880px;top:100px;width:180px;height:170px"></div>

  <div class="card" style="left:41px;top:112px;width:351px;height:141px">
    <div class="card-title" style="padding-top:8px"><span class="ico"><svg viewBox="0 0 32 32"><circle cx="15" cy="17" r="12"/><circle cx="15" cy="17" r="7"/><circle cx="15" cy="17" r="2"/><path d="M15 17L27 5M23 5h4v4"/></svg></span>Starting Point</div>
    <ul class="bul">
      <li>Competing energy and infrastructure technologies</li>
      <li>Multiple, partly conflicting decision criteria</li>
      <li>Conflict of sustainability goals</li>
      <li>Need for scenario-specific and transparent decision support</li>
    </ul>
  </div>
  <div class="tri-r abs" style="left:409px;top:173px"></div>
  <div class="card" style="left:440px;top:112px;width:350px;height:141px">
    <div class="card-title" style="padding-top:8px"><span class="ico"><svg viewBox="0 0 32 32"><ellipse cx="16" cy="7" rx="10" ry="4"/><path d="M6 7v18c0 2 4 4 10 4s10-2 10-4V7M6 13c0 2 4 4 10 4s10-2 10-4M6 19c0 2 4 4 10 4s10-2 10-4"/></svg></span>Methodological Foundations</div>
    <ul class="bul">
      <li>Raw input parameters and KPI definitions</li>
      <li>Representative values from realistic datasets</li>
      <li>Weighting scheme and scenario assumptions</li>
      <li>Literature, simulation and measurement data integrated</li>
    </ul>
  </div>

  <div class="step" style="left:41px;background:var(--lime-soft)">
    <span class="num">1</span>
    <div class="card-title"><span class="ico"><svg viewBox="0 0 32 32"><rect x="6" y="3" width="20" height="26" rx="2"/><rect x="9" y="6" width="14" height="5"/><path d="M10 15h2M15 15h2M20 15h2M10 19h2M15 19h2M20 19h2M10 23h2M15 23h2M20 23h2"/></svg></span>KPI Calculation</div>
    <ul class="bul"><li>Derive relevant KPIs from input parameters</li><li>Cover technical, economic, ecological, social and socio-economic dimensions</li><li>Ensure technology-specific metrics</li></ul>
  </div>
  <div class="step" style="left:257px;background:var(--grey-soft);border-color:var(--border-grey)">
    <span class="num">2</span>
    <div class="card-title" style="border-color:#c8c8c8"><span class="ico" style="color:#555"><svg viewBox="0 0 32 32"><path d="M8 3v26M16 3v26M24 3v26"/><circle cx="8" cy="20" r="2.5" fill="#f3f3f3"/><circle cx="16" cy="11" r="2.5" fill="#f3f3f3"/><circle cx="24" cy="18" r="2.5" fill="#f3f3f3"/></svg></span>Normalization</div>
    <ul class="bul"><li>Convert heterogeneous KPI scales to a common scale</li><li>Min–max normalization to 0–100</li><li>Enable consistent comparison of metrics</li></ul>
  </div>
  <div class="step" style="left:473px;background:var(--teal-soft);border-color:#7fa89c">
    <span class="num">3</span>
    <div class="card-title" style="border-color:#8fb2a8"><span class="ico" style="color:var(--teal)"><svg viewBox="0 0 32 32"><circle cx="16" cy="16" r="14"/><path d="M9 24v-5M14 24v-8M19 24v-10M24 24v-13M8 15l7-5 4 2 6-5"/></svg></span>Weighting &amp;<br>Aggregation</div>
    <ul class="bul"><li>Weight criteria according to scenario priorities</li><li>Aggregate into an overall score</li><li>Ensure transparency of assumptions</li></ul>
  </div>
  <div class="step" style="left:689px;background:var(--grey-soft);border-color:var(--border-grey)">
    <span class="num">4</span>
    <div class="card-title" style="border-color:#c8c8c8"><span class="ico" style="color:#555"><svg viewBox="0 0 32 32"><circle cx="16" cy="16" r="14"/><path d="M5 22c4 0 6-12 11-12s7 12 11 12M16 10v12" stroke-dasharray="2 2"/></svg></span>Sensitivity &amp;<br>Uncertainty<br>Analysis</div>
    <ul class="bul"><li>Monte Carlo simulation of uncertain inputs</li><li>Test robustness of results</li><li>Analyze influence of key assumptions and weightings</li></ul>
  </div>
  <div class="step" style="left:905px;background:var(--lime-soft)">
    <span class="num">5</span>
    <div class="card-title"><span class="ico"><svg viewBox="0 0 32 32"><path d="M10 4h12v8a6 6 0 01-12 0zM10 6H5c0 4 2 7 5 7M22 6h5c0 4-2 7-5 7M16 18v5M11 28h10l-1-5h-8z"/></svg></span>Ranking &amp;<br>Interpretation</div>
    <ul class="bul"><li>Rank technology options</li><li>Identify trade-offs and hotspots</li><li>Provide clear, actionable insights</li></ul>
  </div>
  <div class="tri-d abs" style="left:130px;top:454px"></div>
  <div class="tri-d abs" style="left:346px;top:454px"></div>
  <div class="tri-d abs" style="left:562px;top:454px"></div>
  <div class="tri-d abs" style="left:778px;top:454px"></div>
  <div class="tri-d abs" style="left:994px;top:454px"></div>

  <div class="bar" style="left:41px;top:468px;width:1055px;height:90px;display:flex;align-items:center">
    <div style="width:94px;display:flex;justify-content:center;border-right:1px solid rgba(255,255,255,.35);height:70px;align-items:center">
      <div class="round-ico" style="width:66px;height:66px"><svg width="36" height="36" viewBox="0 0 32 32"><rect x="7" y="5" width="18" height="24" rx="2"/><path d="M12 5V3h8v2M10 12l2 2 3-3M17 12h5M10 19l2 2 3-3M17 19h5"/><circle cx="24" cy="25" r="4"/><path d="M22 25l1.5 1.5 2.5-3"/></svg></div>
    </div>
    <div style="flex:1;padding-left:14px">
      <div class="bar-title" style="font-size:17px;margin-bottom:8px">Integrated MCDA Assessment – Transparent, Robust, Decision-Ready</div>
      <div style="display:flex">
        <div class="mcda-item" style="border-left:none;padding-left:0"><svg viewBox="0 0 32 32" fill="none" stroke="#fff" stroke-width="1.6"><path d="M16 4v24M10 28h12M5 8h22M5 8l-4 10h8zM27 8l-4 10h8zM1 18a4 3 0 008 0M23 18a4 3 0 008 0"/></svg>Structured comparison of alternatives across multiple dimensions</div>
        <div class="mcda-item"><svg viewBox="0 0 32 32" fill="none" stroke="#fff" stroke-width="1.6"><circle cx="13" cy="13" r="10"/><path d="M20 20l9 9M6 13c3-4 11-4 14 0-3 4-11 4-14 0z"/><circle cx="13" cy="13" r="2"/></svg>Identification of trade-offs and hotspots</div>
        <div class="mcda-item"><svg viewBox="0 0 32 32" fill="none" stroke="#fff" stroke-width="1.6"><path d="M16 3l11 4v8c0 7-5 12-11 14C10 27 5 22 5 15V7zM11 16l4 4 6-7"/></svg>Robust results under uncertainty and sensitivity</div>
        <div class="mcda-item"><svg viewBox="0 0 32 32" fill="none" stroke="#fff" stroke-width="1.6"><circle cx="8" cy="12" r="3"/><circle cx="16" cy="9" r="3.5"/><circle cx="24" cy="12" r="3"/><path d="M2 24c0-4 3-6 6-6M30 24c0-4-3-6-6-6M9 26c0-5 3-8 7-8s7 3 7 8z"/></svg>Support for strategic, scientific and investment decisions</div>
        <div class="mcda-item"><svg viewBox="0 0 32 32" fill="none" stroke="#fff" stroke-width="1.6"><rect x="3" y="4" width="26" height="18" rx="1"/><path d="M12 28h8M16 22v6M7 18v-3M11 18v-6M8 10a3 3 0 100-.1M17 9h8M17 13h8M17 17h6"/></svg>Suitable for scenario studies, method comparisons and interactive dashboards</div>
      </div>
    </div>
  </div>

  <div class="footer"><svg width="11" height="11" viewBox="0 0 12 12" fill="none" stroke="#5b7a0c"><circle cx="6" cy="6" r="5"/><path d="M1 6h10M6 1c-2 2-2 8 0 10M6 1c2 2 2 8 0 10"/></svg>Broadly applicable to diverse technologies, processes and products</div>
  <div class="footer-line"></div>
  <div class="brand"><span class="brand-dot"></span>Moorwaldinstitut Graz</div>
</section>

<!-- ============ SLIDE 3 ============ -->
<section class="slide slide--pre">
  <header class="hdr">
    <h2>Conceptual Pre-engineering</h2>
    <p>Structured process for developing robust, sustainable energy technology projects</p>
  </header>

  <div class="chevrons">
    <div class="chev" style="left:41px;width:217px;background:var(--green)"><span class="n">1</span>OBJECTIVES &amp;<br>BOUNDARY CONDITIONS</div>
    <div class="chev" style="left:244px;width:224px;background:var(--green-2)"><span class="n">2</span>CONCEPT<br>DEVELOPMENT</div>
    <div class="chev" style="left:454px;width:224px;background:var(--green-3)"><span class="n">3</span>TECHNO-ECONOMIC<br>ASSESSMENT (TEA)</div>
    <div class="chev" style="left:664px;width:224px;background:var(--grey-dark)"><span class="n">4</span>RISK ASSESSMENT</div>
    <div class="chev" style="left:874px;width:222px;background:var(--grey-mid)"><span class="n">5</span>CONCEPT VALIDATION &amp;<br>RECOMMENDATION</div>
  </div>

  <div class="col" style="left:41px;width:213px">
    <span class="ico" style="width:40px;height:40px"><svg viewBox="0 0 32 32"><circle cx="15" cy="17" r="12"/><circle cx="15" cy="17" r="7"/><circle cx="15" cy="17" r="2"/><path d="M15 17L27 5M23 5h4v4"/></svg></span>
    <ul class="bul"><li>Problem definition and project goals</li><li>Stakeholders and requirements</li><li>Legal and regulatory framework</li><li>System boundaries and assessment scope</li></ul>
  </div>
  <div class="col" style="left:254px;width:201px">
    <span class="ico" style="width:40px;height:40px"><svg viewBox="0 0 32 32"><path d="M12 21c0-4-4-5-4-10a8 8 0 0116 0c0 5-4 6-4 10zM13 25h6M14 28h4M16 0v1M5 5l2 2M27 5l-2 2M2 13h2M28 13h2"/></svg></span>
    <ul class="bul"><li>Technology screening</li><li>System and process concepts</li><li>Option development</li><li>Innovation and technology integration</li></ul>
  </div>
  <div class="col" style="left:455px;width:210px">
    <span class="ico" style="width:40px;height:40px"><svg viewBox="0 0 32 32"><path d="M3 29v-8M9 29v-12M15 29v-16M21 16V8"/><circle cx="25" cy="24" r="4"/><path d="M25 17v2M25 29v2M18 24h2M30 24h2"/></svg></span>
    <ul class="bul"><li>Technical feasibility</li><li>Energy and mass balances</li><li>Capacity and design calculations</li><li>CAPEX and OPEX</li><li>Economic indicators (NPV, IRR, LCOE, LCOX¹)</li></ul>
  </div>
  <div class="col" style="left:665px;width:225px">
    <span class="ico" style="width:40px;height:40px"><svg viewBox="0 0 32 32"><circle cx="13" cy="13" r="11"/><path d="M21 21l9 9M13 6l6 11H7zM13 10v3M13 15v.5"/></svg></span>
    <ul class="bul"><li>Technical and economic risks (e.g. TRL, reliability)</li><li>Environmental and social aspects (incl. LCA, S-LCA²)</li><li>Market, financing and regulatory risks</li><li>Stakeholder acceptance and sociotechnical aspects</li><li>Sensitivity and uncertainty analysis</li></ul>
  </div>
  <div class="col" style="left:890px;width:206px">
    <span class="ico" style="width:40px;height:40px"><svg viewBox="0 0 32 32"><rect x="7" y="4" width="18" height="25" rx="2"/><path d="M12 4V2h8v2M11 11h2M15 11h6M11 16h2M15 16h6M11 21h2M15 21h6"/></svg></span>
    <ul class="bul"><li>Comparison of concept variants</li><li>Recommendation and strategic roadmap</li><li>Go / no-go basis for decision</li><li>Basic engineering as starting point for future upscaling and operation considerations</li></ul>
  </div>

  <div class="methods">
    <div class="method"><span class="ico"><svg viewBox="0 0 32 32"><path d="M6 3h14l6 6v20H6zM20 3v6h6"/><circle cx="15" cy="19" r="5"/><path d="M19 23l5 5"/></svg></span>Literature &amp;<br>data review</div>
    <div class="method"><span class="ico"><svg viewBox="0 0 32 32"><ellipse cx="16" cy="7" rx="10" ry="4"/><path d="M6 7v18c0 2 4 4 10 4s10-2 10-4V7M6 13c0 2 4 4 10 4s10-2 10-4M6 19c0 2 4 4 10 4s10-2 10-4"/></svg></span>Techno-economic<br>analysis (TEA)</div>
    <div class="method"><span class="ico"><svg viewBox="0 0 32 32"><circle cx="16" cy="16" r="13"/><path d="M10 22c2-8 8-12 13-13-1 6-5 12-13 13zM10 22l6-6"/></svg></span>eLife Cycle<br>Assessment<br>(eLCA¹)</div>
    <div class="method"><span class="ico"><svg viewBox="0 0 32 32"><circle cx="8" cy="12" r="3"/><circle cx="16" cy="9" r="3.5"/><circle cx="24" cy="12" r="3"/><path d="M2 24c0-4 3-6 6-6M30 24c0-4-3-6-6-6M9 26c0-5 3-8 7-8s7 3 7 8z"/></svg></span>Social Life Cycle<br>Assessment<br>(S-LCA²)</div>
    <div class="method"><span class="ico"><svg viewBox="0 0 32 32"><path d="M16 4v24M10 28h12M5 8h22M5 8l-4 10h8zM27 8l-4 10h8zM1 18a4 3 0 008 0M23 18a4 3 0 008 0"/></svg></span>Multi-criteria<br>analysis (MCA)</div>
    <div class="method"><span class="ico"><svg viewBox="0 0 32 32"><path d="M4 29v-6M10 29v-9M16 29v-12M22 29v-15M3 17l8-6 5 3 10-9M22 5h4v4"/></svg></span>Risk analysis<br>(qualitative /<br>quantitative)</div>
    <div class="method"><span class="ico"><svg viewBox="0 0 32 32"><path d="M3 3v26h26M6 22l6-8 5 4 9-11M6 26l7-5 5 2 9-8"/></svg></span>Scenario<br>analysis</div>
    <div class="method"><span class="ico"><svg viewBox="0 0 32 32"><circle cx="12" cy="13" r="4"/><path d="M12 3v4M12 19v4M2 13h4M18 13h4M5 6l3 3M16 17l3 3M19 6l-3 3M8 17l-3 3"/><circle cx="24" cy="24" r="3"/><path d="M24 18v2M24 28v2M18 24h2M28 24h2"/></svg></span>Validating<br>process<br>simulation</div>
  </div>

  <div class="kr-line" style="left:41px;width:470px"></div>
  <div class="kr-line" style="left:626px;width:470px"></div>
  <div class="kr-label">KEY RESULTS</div>

  <div class="result" style="left:41px;width:191px"><span class="ico"><svg viewBox="0 0 32 32"><path d="M4 28c0-12 8-22 24-24-1 15-10 22-22 22M6 26l12-12"/></svg></span><div><h4>TECHNICAL CONCEPT</h4><p>Feasible process concept incl. design basis and operating strategy</p></div></div>
  <div class="result" style="left:242px;width:219px"><span class="ico"><svg viewBox="0 0 32 32"><circle cx="15" cy="17" r="12"/><circle cx="15" cy="17" r="7"/><circle cx="15" cy="17" r="2"/><path d="M15 17L27 5M23 5h4v4"/></svg></span><div><h4>ECONOMIC ASSESSMENT</h4><p>Cost estimation, economic viability and key performance indicators</p></div></div>
  <div class="result" style="left:470px;width:225px"><span class="ico"><svg viewBox="0 0 32 32"><circle cx="16" cy="16" r="13"/><path d="M21 10a7 7 0 100 12M9 14h9M9 18h9"/></svg></span><div><h4>SUSTAINABILITY PROFILE</h4><p>Environmental and social impacts across the life cycle, hotspots and improvement potential</p></div></div>
  <div class="result" style="left:705px;width:175px"><span class="ico"><svg viewBox="0 0 32 32"><path d="M16 3l14 26H2zM16 12v9M16 24v1"/></svg></span><div><h4>RISK PROFILE</h4><p>Identified risks, likelihood and mitigation measures</p></div></div>
  <div class="result" style="left:889px;width:207px"><span class="ico"><svg viewBox="0 0 32 32"><path d="M20 3v12M20 3h9l-3 3 3 3h-9M4 28c6 0 8-4 4-7s2-6 12-6"/><circle cx="4" cy="28" r="2"/></svg></span><div><h4>IMPLEMENTATION<br>ROADMAP</h4><p>Milestones, next steps and development path toward realization</p></div></div>

  <div class="bar" style="left:41px;top:490px;width:1055px;height:70px">
    <div class="bar-title" style="text-align:center;font-size:13px;margin-top:4px">BENEFITS OF CONCEPTUAL PRE-ENGINEERING</div>
    <div style="display:flex;margin-top:6px;padding-left:12px">
      <div class="ben-item" style="width:250px"><svg viewBox="0 0 32 32"><circle cx="16" cy="16" r="13"/><path d="M10 16l4 4 8-9"/></svg>Sound basis for decisions through integrated evaluation of technical, economic, environmental and social aspects</div>
      <div class="ben-item" style="width:212px"><svg viewBox="0 0 32 32"><path d="M3 26l9-9 5 5 12-13M22 9h7v7"/></svg>Early reduction of technical, economic and sustainability risks</div>
      <div class="ben-item" style="width:176px"><svg viewBox="0 0 32 32"><circle cx="16" cy="16" r="13"/><path d="M16 8v8l5 4"/></svg>Time and cost efficiency through structured and transparent planning</div>
      <div class="ben-item" style="width:188px"><svg viewBox="0 0 32 32"><circle cx="8" cy="12" r="3"/><circle cx="16" cy="9" r="3.5"/><circle cx="24" cy="12" r="3"/><path d="M2 24c0-4 3-6 6-6M30 24c0-4-3-6-6-6M9 26c0-5 3-8 7-8s7 3 7 8z"/></svg>Tailored solutions for project-specific conditions and stakeholder needs</div>
      <div class="ben-item" style="flex:1"><svg viewBox="0 0 32 32"><path d="M4 28c0-12 8-22 24-24-1 15-10 22-22 22M6 26l12-12"/></svg>Holistic view including non-economic benefits and long-term impact considerations</div>
    </div>
  </div>

  <div class="footer"><svg width="11" height="11" viewBox="0 0 12 12" fill="none" stroke="#5b7a0c"><circle cx="6" cy="6" r="5"/><path d="M1 6h10M6 1c-2 2-2 8 0 10M6 1c2 2 2 8 0 10"/></svg>Broadly applicable to diverse technologies, processes and products</div>
  <div class="footer-line"></div>
  <div class="brand"><span class="brand-dot"></span>Moorwaldinstitut Graz</div>
</section>

</body>
</html>
```